Design for exciting christmas promotional offer from a jewellery store

Christmas offer. Get a free solid sterling silver bangle with every $100 purchase. Choice of 3 bangles- infinity, feather and tree of life.

Attaching pictures of bangles in two angles. The main poster is of size 1000x1194mm (h x w). Also the same concept needs to be done on A0 size and 830x2000mm (w x h).

The brand is 'Valdemoro'- we use 'Perpetua' font for brand name. Also attaching the logo that can be used if design permits (higher version of logo can also be provided).

The poster needs to look beautiful & elegant. Christmas feel should be apparent.
Updates

Hi all- just wanted to thank all designers for their efforts. There were some wonderful designs and we have gone ahead and made our selection.Thanks again for all your contribution.Cheers. Added Monday, November 21, 2016

Target Market(s)

Jewellery retail; target group: female (18-60 yrs). Premium silver and gold jewellery.

Industry/Entity Type

Jewelry

Requirements
Must have
• Christmas decoration; ribbon.

```html
<!DOCTYPE html>
<html lang="en">
<head>
<meta charset="utf-8">
<title>Christmas Offer – Valdemoro</title>
<link rel="stylesheet" href="https://fonts.googleapis.com/css2?family=Alegreya+Sans:wght@400;500&family=Parisienne&family=IM+Fell+DW+Pica+SC&display=swap">
<style>
  :root {
    --page: #e3e3e3;
    --magenta: #c41656;
    --magenta-deep: #8c0f3c;
    --night: #0b0b0b;
    --olive: #bfbf00;
    --footer-grey: #808080;
    --white: #ffffff;
    --dome-rim: #b5b5b5;
    --silver: #b9b9b9;
    --silver-ink: #5a5a5a;
  }
  * { margin: 0; padding: 0; box-sizing: border-box; }
  html, body { width: 1200px; height: 1200px; overflow: hidden; background: var(--page); }
  .poster {
    position: absolute; left: 30px; top: 113px; width: 1127px; height: 943px;
    background: var(--night); overflow: hidden;
    font-family: "Alegreya Sans", sans-serif; color: var(--white);
  }
  .hero-photo {
    position: absolute; left: 0; top: 263px; width: 1127px; height: 524px;
    background:
      radial-gradient(ellipse 55% 70% at 68% 45%, #c01a52 0%, #8a0f38 45%, rgba(20,4,10,0) 80%),
      linear-gradient(90deg, #0b0b0b 0%, #1a0a10 40%, #3a0a1c 100%);
  }
  .header { position: absolute; left: 0; top: 0; width: 1127px; height: 430px; }
  .headline {
    position: absolute; left: 70px; top: 30px;
    font-family: "Parisienne", cursive; font-size: 178px; line-height: 1; font-weight: 400;
    color: var(--white); white-space: nowrap;
  }
  .brand-seal {
    position: absolute; left: 996px; top: 176px; width: 116px; height: 116px; border-radius: 50%;
    background: radial-gradient(circle at 40% 35%, #e2e2e2, var(--silver) 70%);
    display: flex; align-items: center; justify-content: center;
  }
  .brand-name { font-family: "Alegreya Sans", sans-serif; font-size: 20px; font-weight: 500; color: var(--silver-ink); }
  .offer { position: absolute; left: 0; top: 325px; }
  .free-pill {
    position: absolute; left: 0; top: 0; width: 274px; height: 76px;
    background: var(--olive); border-radius: 0 38px 38px 0;
  }
  .offer-line { position: absolute; white-space: nowrap; font-size: 66px; line-height: 1; font-weight: 400; }
  .offer-free { left: 78px; top: 4px; }
  .offer-solid { left: 298px; top: 4px; }
  .offer-item { left: 78px; top: 90px; }
  .bangle-label {
    position: absolute; top: 553px; width: 300px; text-align: center;
    font-family: "IM Fell DW Pica SC", serif; font-size: 40px; line-height: 1;
  }
  .domes { position: absolute; left: 0; top: 0; }
  .footer-rule { position: absolute; left: 0; top: 787px; width: 1127px; height: 14px; background: var(--night); }
  .footer {
    position: absolute; left: 0; top: 801px; width: 1127px; height: 142px; background: var(--footer-grey);
    display: flex; align-items: center; justify-content: center;
    font-size: 90px; letter-spacing: 1px; line-height: 1;
  }
</style>
</head>
<body>
<main class="poster">
  <div class="hero-photo" role="img" aria-label="Photograph of a hand in a red satin glove wearing a silver ring, on a dark background with faint snowflakes"></div>

  <svg class="header" width="1127" height="430" viewBox="0 0 1127 430" aria-hidden="true">
    <path d="M0 0 H1127 V263 H960 C900 300 840 318 788 318 C736 318 680 300 625 263 H0 Z" fill="var(--magenta)"/>
    <path d="M0 263 H625 C680 300 736 318 788 318 C840 318 900 300 960 263 H1127" fill="none" stroke="var(--white)" stroke-width="3"/>
  </svg>

  <h1 class="headline">Christmas Offer</h1>

  <div class="brand-seal"><span class="brand-name">Valdemoro</span></div>

  <div class="offer">
    <div class="free-pill"></div>
    <p class="offer-line offer-free">FREE</p>
    <p class="offer-line offer-solid">Solid</p>
    <p class="offer-line offer-item">Sterling Silver Bangle</p>
  </div>

  <p class="bangle-label" style="left:52px">Feather</p>
  <p class="bangle-label" style="left:414px">Tree Of Life</p>
  <p class="bangle-label" style="left:774px">Infinity</p>

  <svg class="domes" width="1127" height="787" viewBox="0 0 1127 787" aria-hidden="true">
    <defs><clipPath id="dome-clip"><rect x="0" y="0" width="1127" height="787"/></clipPath></defs>
    <g clip-path="url(#dome-clip)">
      <ellipse cx="202" cy="800" rx="196" ry="200" fill="var(--white)" stroke="var(--dome-rim)" stroke-width="10"/>
      <ellipse cx="564" cy="806" rx="196" ry="200" fill="var(--white)" stroke="var(--dome-rim)" stroke-width="10"/>
      <ellipse cx="924" cy="806" rx="196" ry="200" fill="var(--white)" stroke="var(--dome-rim)" stroke-width="10"/>
    </g>
  </svg>

  <div role="img" aria-label="Silver feather bangle" style="position:absolute;left:80px;top:650px;width:250px;height:110px;border-radius:50%;background:radial-gradient(ellipse at center,#f4f4f4 40%,#e2e2e2 70%,rgba(255,255,255,0) 72%)"></div>
  <div role="img" aria-label="Silver tree of life bangle" style="position:absolute;left:440px;top:655px;width:250px;height:110px;border-radius:50%;background:radial-gradient(ellipse at center,#f4f4f4 40%,#e2e2e2 70%,rgba(255,255,255,0) 72%)"></div>
  <div role="img" aria-label="Silver infinity bangle" style="position:absolute;left:800px;top:655px;width:250px;height:110px;border-radius:50%;background:radial-gradient(ellipse at center,#f4f4f4 40%,#e2e2e2 70%,rgba(255,255,255,0) 72%)"></div>

  <div class="footer-rule"></div>
  <p class="footer">With Every $100 Purchase</p>
</main>
</body>
</html>
```